2 Creative Website Banners for Furniture Brand

Morning Tobrasca....
The get a great night sleep banner is complete - we are happy with that one.
Ive uploaded a slightly different concept for the other banner below. This is just something rough ive thrown together. But you can see I have added a curve, a maroon coloured background which is slightly transparent and a big heart in the background....
I do not necessarily want to use this heart image but something a bit like this (a nice graphic, gif etc) but something quite elegant faded in, or perhaps a number of hearts (done in a tasteful way). Also can we keep the typography in the same format as you can see for this one.
Nearly there :)!
Industry/Entity Type
Furniture

```html
<!DOCTYPE html>
<html lang="en">
<head>
<meta charset="utf-8">
<title>Corvale Furniture – Find a look you love</title>
<link href="https://fonts.googleapis.com/css2?family=Cormorant+Garamond:wght@400;500;700&family=Josefin+Sans:wght@300;400&family=Raleway:wght@400;500&family=Roboto:wght@300&display=swap" rel="stylesheet">
<style>
  :root {
    --notice-bg: #e4dee1;
    --notice-text: #a8915f;
    --header-bg: #ffffff;
    --brand-plum: #2f1c2b;
    --phone-text: #2b2430;
    --utility-text: #6e6470;
    --gold: #c9ad3f;
    --nav-bg: #6b5559;
    --nav-text: #f3eced;
    --hero-dark: #2f2a30;
    --hero-mid: #4b4751;
    --hero-warm: #5c4c52;
    --band-maroon: rgba(88, 34, 52, 0.72);
    --heart-line: rgba(255, 225, 232, 0.22);
    --hero-text: #ffffff;
    --button-bg: #6b5559;
  }
  * { margin: 0; padding: 0; box-sizing: border-box; }
  html, body { width: 1200px; height: 493px; overflow: hidden; background: var(--header-bg); }
  .page { position: relative; width: 1200px; height: 493px; }

  .notice-bar {
    position: absolute; top: 0; left: 0; width: 1200px; height: 20px;
    background: var(--notice-bg); color: var(--notice-text);
    font: 400 9px/20px "Raleway", sans-serif; text-align: center; letter-spacing: 0.1px;
  }

  .site-header { position: absolute; top: 20px; left: 0; width: 1200px; height: 82px; background: var(--header-bg); }
  .brand {
    position: absolute; left: 43px; top: 22px;
    display: flex; align-items: center; gap: 10px;
    font: 300 28px/1 "Josefin Sans", sans-serif; letter-spacing: 6px; color: var(--brand-plum);
  }
  .brand-mark { width: 8px; height: 8px; background: var(--brand-plum); }

  .phone {
    position: absolute; right: 45px; top: 9px;
    display: flex; align-items: center; gap: 10px;
    font: 300 21px/1 "Roboto", sans-serif; color: var(--phone-text); letter-spacing: 0.5px;
  }
  .utility-links {
    position: absolute; right: 52px; top: 54px;
    display: flex; align-items: center; gap: 16px; list-style: none;
    font: 400 8.5px/1 "Josefin Sans", sans-serif; color: var(--utility-text);
  }
  .utility-links li { display: flex; align-items: center; gap: 5px; }
  .cart-count { color: var(--phone-text); margin-left: 3px; }

  .main-nav { position: absolute; top: 102px; left: 0; width: 1200px; height: 36px; background: var(--nav-bg); }
  .main-nav ul { list-style: none; }
  .main-nav li {
    position: absolute; top: 0; transform: translateX(-50%);
    font: 500 11px/36px "Raleway", sans-serif; color: var(--nav-text); white-space: nowrap;
    display: flex; align-items: center; gap: 8px;
  }

  .hero {
    position: absolute; top: 138px; left: 0; width: 1200px; height: 355px; overflow: hidden;
    background: linear-gradient(90deg, var(--hero-dark) 0%, var(--hero-mid) 22%, var(--hero-mid) 48%, var(--hero-warm) 62%, var(--hero-dark) 100%);
  }
  .hero-photo { position: absolute; inset: 0; }
  .hero-band { position: absolute; left: 0; top: 150px; width: 1200px; height: 171px; }
  .hero-title {
    position: absolute; left: 0; width: 1200px; top: 177px; text-align: center;
    font: 400 60px/1 "Cormorant Garamond", serif; color: var(--hero-text);
  }
  .hero-sub {
    position: absolute; left: 0; width: 1200px; top: 237px; text-align: center;
    font: 400 14.5px/17.5px "Cormorant Garamond", serif; color: var(--hero-text);
  }
  .hero-button {
    position: absolute; left: 543px; top: 290px; width: 114px; height: 20px;
    background: var(--button-bg); border: 1px solid #cfc3c6; color: var(--hero-text);
    font: 700 10px/18px "Cormorant Garamond", serif; text-align: center; letter-spacing: 0.3px;
  }
</style>
</head>
<body>
<div class="page">
  <div class="notice-bar">COVID 19 - WE ARE TAKING ORDERS AND DELIVERING AS NORMAL</div>

  <header class="site-header">
    <div class="brand"><span class="brand-name">CORVALE</span><span class="brand-mark"></span></div>

    <div class="phone">
      <svg width="20" height="20" viewBox="0 0 20 20" aria-hidden="true">
        <circle cx="10" cy="10" r="10" fill="#2a3f8f"/>
        <path d="M3 3 L17 17 M17 3 L3 17" stroke="#fff" stroke-width="3"/>
        <path d="M3 3 L17 17 M17 3 L3 17" stroke="#d02030" stroke-width="1"/>
        <path d="M10 0 V20 M0 10 H20" stroke="#fff" stroke-width="5"/>
        <path d="M10 0 V20 M0 10 H20" stroke="#d02030" stroke-width="3"/>
      </svg>
      <span>0345 210 7768</span>
    </div>

    <ul class="utility-links">
      <li>
        <svg width="12" height="12" viewBox="0 0 12 12" aria-hidden="true"><circle cx="6" cy="6" r="5" fill="none" stroke="var(--gold)" stroke-width="1.4"/></svg>
        TRACK ORDER
      </li>
      <li>
        <svg width="14" height="12" viewBox="0 0 14 12" aria-hidden="true"><path d="M7 12 L1.2 5.8 A3.3 3.3 0 0 1 7 2 A3.3 3.3 0 0 1 12.8 5.8 Z" fill="var(--gold)"/></svg>
        MY WISHLIST
      </li>
      <li>
        <svg width="13" height="14" viewBox="0 0 13 14" aria-hidden="true"><rect x="1" y="4" width="11" height="9" fill="none" stroke="var(--gold)" stroke-width="1.2"/><path d="M4 4 V2.5 A2.5 2.5 0 0 1 9 2.5 V4" fill="none" stroke="var(--gold)" stroke-width="1.2"/></svg>
        CART <span class="cart-count">(0)</span>
      </li>
    </ul>
  </header>

  <nav class="main-nav">
    <ul>
      <li style="left:276px">HOME</li>
      <li style="left:408px">BEDROOM <svg width="8" height="5" viewBox="0 0 8 5" aria-hidden="true"><path d="M1 1 L4 4 L7 1" fill="none" stroke="currentColor" stroke-width="1.3"/></svg></li>
      <li style="left:570px">LIVING ROOM <svg width="8" height="5" viewBox="0 0 8 5" aria-hidden="true"><path d="M1 1 L4 4 L7 1" fill="none" stroke="currentColor" stroke-width="1.3"/></svg></li>
      <li style="left:742px">DINING ROOM <svg width="8" height="5" viewBox="0 0 8 5" aria-hidden="true"><path d="M1 1 L4 4 L7 1" fill="none" stroke="currentColor" stroke-width="1.3"/></svg></li>
      <li style="left:905px">CONTACT <svg width="8" height="5" viewBox="0 0 8 5" aria-hidden="true"><path d="M1 1 L4 4 L7 1" fill="none" stroke="currentColor" stroke-width="1.3"/></svg></li>
    </ul>
  </nav>

  <section class="hero">
    <div class="hero-photo" role="img" aria-label="Dark styled bedroom with mirrored dressing table, ornate mirror, glass jars, orchids, upholstered bed and bedside lamp"></div>

    <svg class="hero-band" viewBox="0 0 1200 171" preserveAspectRatio="none" aria-hidden="true">
      <defs>
        <path id="heart" d="M0 14 C-4 9 -14 4 -14 -4 A7 7 0 0 1 0 -8 A7 7 0 0 1 14 -4 C14 4 4 9 0 14 Z"/>
      </defs>
      <path d="M0 32 Q600 -18 1200 32 L1200 171 L0 171 Z" fill="var(--band-maroon)"/>
      <path d="M0 32 Q600 -18 1200 32" fill="none" stroke="rgba(255,225,232,0.35)" stroke-width="1"/>
      <g fill="none" stroke="var(--heart-line)" stroke-width="1.2">
        <use href="#heart" transform="translate(170 95) scale(2.6)"/>
        <use href="#heart" transform="translate(250 132) scale(1.3)"/>
        <use href="#heart" transform="translate(95 140) scale(0.9)"/>
        <use href="#heart" transform="translate(1030 92) scale(2.6)"/>
        <use href="#heart" transform="translate(950 134) scale(1.3)"/>
        <use href="#heart" transform="translate(1110 142) scale(0.9)"/>
      </g>
    </svg>

    <h1 class="hero-title">FIND a look you LOVE</h1>
    <p class="hero-sub">Lorem ipsum not sure what the rest of<br>this will say at the moment</p>
    <div class="hero-button">SHOP BEDROOMS</div>
  </section>
</div>
</body>
</html>
```